Divorce Lawyer print and ebook cover (Lanterns over the quiet harbor )

I need a front and back cover for my divorce and family law book. I already have a photo and title. The back cover photo is not necessary but can be interesting the Front-main cover is a must

Target Market(s)

Prospective client

Colors

Designer to choose colors to be used in the design.

Requirements
Must have
• Front photo by viewable.

```html
<!DOCTYPE html>
<html lang="en">
<head>
<meta charset="utf-8">
<title>Lanterns over the quiet harbor — cover wrap</title>
<link href="https://fonts.googleapis.com/css2?family=Bebas+Neue&family=Arimo:wght@400;700&display=swap" rel="stylesheet">
<style>
  :root {
    --stage: #fdd10a;
    --ink: #050505;
    --accent: #ffd300;
    --paper: #ffffff;
    --rule: #9a9a9a;
  }
  html, body {
    margin: 0;
    width: 1200px;
    height: 1200px;
    overflow: hidden;
    background: var(--stage);
  }
  .stage {
    position: relative;
    width: 1200px;
    height: 1200px;
  }
  .cover-wrap {
    position: absolute;
    left: 40px;
    top: 197px;
    width: 1194px;
    height: 860px;
    transform: scale(0.938);
    transform-origin: 0 0;
  }
  .display { font-family: "Bebas Neue", "Oswald", sans-serif; font-weight: 400; line-height: 0.9; }
  .body-copy { font-family: "Arimo", Arial, sans-serif; text-align: justify; margin: 0 0 19px; }

  /* back cover */
  .back-cover { position: absolute; left: 0; top: 0; width: 573px; height: 860px; background: var(--ink); overflow: hidden; }
  .author-strip { position: absolute; left: 0; top: 0; width: 234px; height: 860px; background: var(--stage); }
  .author-strip .author-name { position: absolute; left: 22px; top: 50px; font-size: 34px; color: var(--ink); letter-spacing: 0.5px; }
  .author-strip .bio { position: absolute; left: 16px; top: 108px; width: 202px; }
  .author-strip .body-copy { font-size: 13px; line-height: 17.5px; color: var(--ink); margin-bottom: 18px; }
  .author-photo { position: absolute; left: 0; top: 470px; width: 234px; height: 234px; border-radius: 50%; background: radial-gradient(circle at 50% 35%, #3a8a95 0 18%, #b9a99a 30%, #7b8a84 60%, #55504a 100%); }

  .back-panel { position: absolute; left: 264px; top: 40px; width: 278px; }
  .back-panel .title-top { font-size: 66px; color: var(--accent); text-align: center; }
  .back-panel .title-mid { display: flex; align-items: center; gap: 8px; font-size: 30px; color: var(--paper); margin: 2px 0 4px; }
  .back-panel .title-mid::before, .back-panel .title-mid::after { content: ""; flex: 1; height: 1px; background: var(--rule); }
  .back-panel .title-bottom { font-size: 58px; color: var(--accent); text-align: center; }
  .back-panel .blurb { margin-top: 34px; }
  .back-panel .body-copy { font-size: 14.5px; line-height: 19.2px; color: var(--paper); }

  /* spine */
  .spine { position: absolute; left: 573px; top: 0; width: 48px; height: 860px; background: var(--stage); }
  .spine-title, .spine-author { position: absolute; left: 10px; writing-mode: vertical-rl; color: var(--ink); font-size: 26px; }
  .spine-title { top: 156px; }
  .spine-author { top: 636px; font-size: 22px; }

  /* front cover */
  .front-cover { position: absolute; left: 621px; top: 0; width: 573px; height: 860px; background: var(--ink); overflow: hidden; }
  .front-photo {
    position: absolute; inset: 0 0 200px 0;
    background:
      radial-gradient(ellipse 55% 45% at 85% 40%, rgba(232,196,40,0.75), rgba(232,196,40,0) 70%),
      radial-gradient(ellipse 60% 40% at 45% 15%, #eef2f3, rgba(238,242,243,0) 75%),
      linear-gradient(180deg, #b9c6b2 0%, #a9b7b8 30%, #7d8a8f 55%, #4b5356 78%, #151616 100%);
  }
  .front-fade { position: absolute; left: 0; right: 0; top: 430px; height: 260px; background: linear-gradient(180deg, rgba(5,5,5,0), var(--ink)); }
  .front-cover .author-name { position: absolute; left: 0; right: 0; top: 22px; text-align: center; font-size: 46px; color: var(--ink); letter-spacing: 1px; }
  .front-title { position: absolute; left: 46px; right: 46px; top: 490px; }
  .front-title .title-top { font-size: 132px; color: var(--accent); text-align: center; }
  .front-title .title-mid { display: flex; align-items: center; gap: 14px; font-size: 58px; color: var(--paper); margin: 6px 0 10px; }
  .front-title .title-mid::before, .front-title .title-mid::after { content: ""; flex: 1; height: 1px; background: var(--rule); }
  .front-title .title-bottom { font-size: 100px; color: var(--accent); text-align: center; }
</style>
</head>
<body>
<main class="stage">
  <section class="cover-wrap">

    <article class="back-cover">
      <aside class="author-strip">
        <h2 class="author-name display">Author’s Name</h2>
        <div class="bio">
          <p class="body-copy">Lorem Ipsum is simply dummy text of the printing and typesetting industry. Lorem Ipsum has been the industry's standard dummy text ever since the 1500s, when an unknown printer took a galley of type and scrambled it to make a type specimen book.</p>
          <p class="body-copy">Lorem Ipsum is simply dummy text of the printing and typesetting industry. Lorem Ipsum has been the industry's standard dummy text ever since the 1500s, when an unknown printer took a galley of type and scrambled it to make a type specimen book.</p>
        </div>
        <div class="author-photo" role="img" aria-label="Round photo of a small child in a knitted hat on a playground swing"></div>
      </aside>

      <div class="back-panel">
        <div class="title-top display">Lanterns</div>
        <div class="title-mid display">Over the</div>
        <div class="title-bottom display">Quiet Harbor</div>
        <div class="blurb">
          <p class="body-copy">Lorem Ipsum is simply dummy text of the printing and typesetting industry. Lorem Ipsum has been the industry's standard dummy text ever since the 1500s, when an unknown printer took a galley of type and scrambled it to make a type specimen book.</p>
          <p class="body-copy">Lorem Ipsum is simply dummy text of the printing and typesetting industry. Lorem Ipsum has been the industry's standard dummy text ever since the 1500s, when an unknown printer took a galley of type and scrambled it to make a type specimen book.</p>
          <p class="body-copy">Lorem Ipsum is simply dummy text of the printing and typesetting industry. Lorem Ipsum has been the industry's standard dummy text ever since the 1500s, when an unknown printer took a galley of type and scrambled it to make a type specimen book.</p>
        </div>
      </div>
    </article>

    <div class="spine">
      <span class="spine-title display">Lanterns over the quiet harbor</span>
      <span class="spine-author display">Author’s Name</span>
    </div>

    <article class="front-cover">
      <div class="front-photo" role="img" aria-label="Photo of a man in a suit standing before a fork in a misty forest road with a two-way signpost"></div>
      <div class="front-fade"></div>
      <h2 class="author-name display">Author’s Name</h2>
      <h1 class="front-title">
        <div class="title-top display">Lanterns</div>
        <div class="title-mid display">Over the</div>
        <div class="title-bottom display">Quiet Harbor</div>
      </h1>
    </article>

  </section>
</main>
</body>
</html>
```